Business Card Design Project

I have a two letter domain name qo.com.au (lower case font please). I want a business card, cum logo that is die cut (around the qo segment at least) that fits standard business card size.
qo is all about what 'I am' - a journalist, blogger, analyst, commentator. My mantra is "I wander so qo'.
The reverse of the card only needs my name Lon Fitch, email lon@qo.com.au and mobile +61 400 555 817
Target Market(s)
Mainly people that will use my professional writing services and suppliers that will provide product for review
Industry/Entity Type
Business
Requirements
Must have
- One side is qo.com.au (hint - the .com.au can be vertical or horizontal to fit - the qo should be as large as possible).
The other requires large size font name, email and phone details (so no one needs glasses to read it).
The die cut can be just to highlight the qo segment - need not be around the whole card.
Font used in the past was Belwe (old style - very much like the i used in the information symbol).
Colours - no preference - prefer two colour to process colour but can also be an outline font instead of solid colour.

```html
<!DOCTYPE html>
<html lang="en">
<head>
<meta charset="utf-8">
<title>qo.com.au business card</title>
<link rel="stylesheet" href="https://fonts.googleapis.com/css2?family=Jost:wght@300;400;600&display=swap">
<style>
  :root {
    --stage: #2a2a2c;
    --brand-blue: #1ea3dc;
    --brand-blue-deep: #1590c8;
    --brand-blue-light: #5cc3ec;
    --paper: #f4f5f6;
    --white: #ffffff;
  }
  * { box-sizing: border-box; margin: 0; padding: 0; }
  html, body {
    width: 1200px;
    height: 900px;
    overflow: hidden;
    background: var(--stage);
    font-family: "Jost", "Futura", sans-serif;
  }
  .canvas {
    position: relative;
    width: 1200px;
    height: 900px;
  }

  /* Reverse side: contact details */
  .card-back {
    position: absolute;
    left: 270px;
    top: 35px;
    width: 660px;
    height: 400px;
    background: linear-gradient(135deg, #2aaee4 0%, var(--brand-blue) 55%, var(--brand-blue-deep) 100%);
    border-radius: 0 200px 200px 0;
    overflow: hidden;
  }
  .corner-accent {
    position: absolute;
    right: 0;
    top: 0;
    width: 300px;
    height: 200px;
    background: radial-gradient(ellipse at 85% 0%, var(--brand-blue-light) 0%, rgba(92, 195, 236, 0) 70%);
  }
  .contact {
    position: absolute;
    left: 56px;
    bottom: 70px;
    color: var(--white);
  }
  .contact-name {
    font-weight: 600;
    font-size: 40px;
    letter-spacing: 0.5px;
    margin-bottom: 22px;
  }
  .contact-line {
    display: flex;
    align-items: center;
    gap: 22px;
    font-weight: 300;
    font-size: 34px;
    line-height: 1;
    margin-bottom: 18px;
  }
  .contact-line svg {
    width: 40px;
    height: 34px;
    flex: none;
  }

  /* Front side: die-cut name */
  .card-front {
    position: absolute;
    left: 270px;
    top: 465px;
    width: 660px;
    height: 400px;
    background: var(--paper);
    border-radius: 200px 0 0 200px;
    overflow: hidden;
  }
  .die-cut-disc {
    position: absolute;
    left: 18px;
    top: 18px;
    width: 364px;
    height: 364px;
    border-radius: 50%;
    background: var(--brand-blue);
  }
  .domain-name {
    position: absolute;
    left: 400px;
    top: 0;
    height: 400px;
    display: flex;
    align-items: center;
    color: var(--brand-blue);
    font-weight: 300;
    font-size: 52px;
    letter-spacing: 1px;
    white-space: nowrap;
  }
</style>
</head>
<body>
<main class="canvas">

  <section class="card-back" aria-label="Card reverse with contact details">
    <div class="corner-accent" role="img" aria-label="Decorative accent area in the top corner"></div>
    <div class="contact">
      <p class="contact-name">Lon Fitch</p>
      <p class="contact-line">
        <svg viewBox="0 0 40 34" aria-hidden="true">
          <rect x="2" y="5" width="36" height="24" fill="none" stroke="#ffffff" stroke-width="3"/>
          <path d="M2 5 L20 20 L38 5" fill="none" stroke="#ffffff" stroke-width="3"/>
        </svg>
        lon@qo.com.au
      </p>
      <p class="contact-line">
        <svg viewBox="0 0 40 34" aria-hidden="true">
          <rect x="10" y="1" width="20" height="32" rx="4" fill="none" stroke="#ffffff" stroke-width="3"/>
          <line x1="17" y1="27" x2="23" y2="27" stroke="#ffffff" stroke-width="3"/>
        </svg>
        +61 400 555 817
      </p>
    </div>
  </section>

  <section class="card-front" aria-label="Card front">
    <div class="die-cut-disc"></div>
    <p class="domain-name">qo.com.au</p>
  </section>

</main>
</body>
</html>
```